The Lune Fox Organic & Natural Soaps needs a good business card

I am sorry for the lack of direction or Scope of the project. I am new at this board.
This is my scope and requirements:
Business card project:
This is related to the Label project I also opened up. (The Lune Fox Organic & Natural Soaps is looking for label designs (along with the business card project (Contest) )
I have attached an initial draft at a logo I tried to come up with for a business card and labelling/marketing. I am hoping that you can take this logo and 'run with it' to finesse it, make it look unique and professional. I am open to new logo ideas.
I am a start up at home company making Organic and Natural Bar soaps, hand soaps, body washes.
All of my ingredients are organic or natural and will include natural essential oils, exfoliants, natural powders/colours, etc.
Some of the names are: Brambelle (feisty, energetic soap), Dunes (more of a sandalwood earthy tones with a sandalwood powder exfoliant), Frost (maybe changing this name - fresh scented), Plum Cedar (lemongrass/ginger, exfoliants), etc....
I am attaching the cardstock I am looking at for packaging as well - this might help with the business card aspect. I was originally just looking at plain kraft paper but am receiving samples of Vera Pindle coloured kraft paper. I may still print business cards on the plain kraft though.. not sure.
If you need more information, please let me know.
Moira
Business Card and Labels
I have come up with a basic logo that I like. If you can finesse it and provide a great business card, that would be great.
I am starting up an at home soap business that will include luxury organic bar soaps, luxury natural olive oil bar soaps, organic hand wash, natural olive oil based body wash. I will be selling online and at shows.
please find attached my logo idea that I would like to incorporate.
I am also looking at packaging/labelling ideas for the bar soaps (prefer kraft cardstock wrap) and labels for the various body washes (natural soap) and the hand washes (organic). The hand washes will be in 250ml square bottles and the body wash will be in tapered bottles (smaller at top going to bottom).
Please let me know if you need more info!
I am also looking for packaging (label design for hand soap/body wash bottles and label design for organic/natural soaps)
This Project coincides with the business card project I also posted: there are 2 projects related - 1) business cards, 2) labels for organic hand wash, natural body wash, sticker label or design for kraft paper to package around luxury organic and natural soaps. I am not sure if a sticker would look nice or the design for the thick kraft paper.
Thank you!
Business card project:
This is related to the Label project I also opened up. (The Lune Fox Organic & Natural Soaps is looking for label designs (along with the business card proje (Contest) )
I have attached an initial draft at a logo I tried to come up with for a business card and labelling/marketing. I am hoping that you can take this logo and 'run with it' to finesse it, make it look unique and professional.
Moira
Hello; I just wanted to let everyone know that if you feel that this
brand needs a different logo, I am open to ideas (if you don't think the
one I started with is ok). I am coming to the experts here!
Just to confirm also - this is related to the label/packaging project, therefore, there are 2 projects, 2 payments! :)
Cheers

```html
<!DOCTYPE html>
<html lang="en">
<head>
<meta charset="utf-8">
<title>The Lune Fox – Soap Box Dieline</title>
<link rel="stylesheet" href="https://fonts.googleapis.com/css2?family=Questrial&family=Fredoka:wght@600&family=Crimson+Text:ital,wght@1,700&family=Arimo:wght@400&display=swap">
<style>
  :root {
    --stage: #f1f1f1;
    --frame: #c9c9c9;
    --die-line: #6f6f6f;
    --flap: #ffffff;
    --kraft: #a8957a;
    --kraft-light: #b09d82;
    --band: #4b3527;
    --lime: #a9bc45;
    --ink: #5a4131;
    --ink-dark: #2c2018;
    --name-yellow: #f3d41b;
    --name-edge: #3a2b12;
    --white: #ffffff;
  }
  html, body {
    margin: 0;
    width: 1200px;
    height: 779px;
    overflow: hidden;
    background: var(--stage);
  }
  .dieline { display: block; width: 1200px; height: 779px; }
  .stage-frame { fill: var(--stage); stroke: var(--frame); stroke-width: 1; }
  .flap { fill: var(--flap); stroke: var(--die-line); stroke-width: 0.8; }
  .panel { fill: var(--kraft); }
  .panel-edge { fill: none; stroke: var(--kraft-light); stroke-width: 0.6; }
  .brand-band { fill: var(--band); }
  .contact-band { fill: var(--lime); }
  .logo-name { font-family: "Questrial", sans-serif; text-anchor: middle; }
  .logo-name--lid { fill: var(--ink); font-size: 34px; }
  .logo-name--band { fill: var(--white); }
  .logo-tagline { font-family: "Questrial", sans-serif; text-anchor: middle; }
  .logo-tagline--lid { fill: var(--ink); font-size: 13.5px; }
  .logo-tagline--band { fill: var(--white); }
  .scent-name {
    font-family: "Fredoka", sans-serif; font-weight: 600; text-anchor: middle;
    fill: var(--name-yellow); stroke: var(--name-edge); stroke-width: 0.6; paint-order: stroke;
  }
  .scent-tagline {
    font-family: "Crimson Text", serif; font-style: italic; font-weight: 700;
    text-anchor: middle; fill: var(--ink-dark);
  }
  .contact-line { font-family: "Arimo", sans-serif; font-size: 7.2px; text-anchor: middle; fill: var(--ink-dark); }
</style>
</head>
<body>
<svg class="dieline" viewBox="0 0 964 626" xmlns="http://www.w3.org/2000/svg">
  <rect class="stage-frame" x="3" y="3" width="958" height="620"/>

  <!-- dust flaps and glue tabs -->
  <path class="flap" d="M375,72 L324,72 Q314,72 314,82 L314,92 Q314,100 322,104 L330,110 Q336,116 336,124 L336,148 L375,148 Z"/>
  <path class="flap" d="M588,72 L631,72 Q641,72 641,82 L641,92 Q641,100 633,104 L625,110 Q619,116 619,124 L619,148 L588,148 Z"/>
  <path class="flap" d="M297,148 L272,148 Q262,148 262,158 L262,288 Q262,298 272,298 L297,298 Z"/>
  <path class="flap" d="M375,298 L330,298 Q314,298 314,310 L314,318 Q314,330 326,334 L336,338 Q344,344 344,354 L344,378 L375,378 Z"/>
  <path class="flap" d="M588,298 L633,298 Q649,298 649,310 L649,318 Q649,330 637,334 L627,338 Q619,344 619,354 L619,378 L588,378 Z"/>
  <path class="flap" d="M668,378 L692,378 Q702,378 702,388 L702,520 Q702,530 692,530 L668,530 Z"/>
  <path class="flap" d="M375,530 L588,530 L585,548 Q584,553 578,553 L385,553 Q379,553 378,548 Z"/>

  <!-- lid panel -->
  <rect class="panel" x="375" y="70" width="213" height="78"/>
  <text class="logo-name logo-name--lid" x="481.5" y="112">The Lune Fox</text>
  <text class="logo-tagline logo-tagline--lid" x="481.5" y="133">Organic &amp; Natural Soaps</text>

  <!-- left side panel -->
  <rect class="panel" x="297" y="148" width="78" height="150"/>
  <rect class="brand-band" x="297" y="174" width="78" height="46"/>
  <text class="logo-name logo-name--band" x="336" y="198" font-size="12">The Lune Fox</text>
  <text class="logo-tagline logo-tagline--band" x="336" y="208" font-size="5.6">Organic &amp; Natural Soaps</text>
  <text class="scent-name" x="336" y="262" font-size="13.5">Brambelle</text>
  <text class="scent-tagline" x="336" y="272" font-size="7">feisty and energetic feel</text>

  <!-- front panel -->
  <rect class="panel" x="375" y="148" width="213" height="150"/>
  <rect class="panel-edge" x="375" y="148" width="213" height="150"/>
  <rect class="brand-band" x="375" y="174" width="213" height="46"/>
  <text class="logo-name logo-name--band" x="481.5" y="200" font-size="22">The Lune Fox</text>
  <text class="logo-tagline logo-tagline--band" x="481.5" y="213" font-size="8.6">Organic &amp; Natural Soaps</text>
  <text class="scent-name" x="481.5" y="266" font-size="20">Brambelle</text>
  <text class="scent-tagline" x="481.5" y="280" font-size="11">feisty and energetic feel</text>

  <!-- contact panel -->
  <rect class="panel" x="375" y="298" width="213" height="80"/>
  <rect class="contact-band" x="375" y="317" width="213" height="41"/>
  <text class="contact-line" x="481.5" y="330">(555) 014-2738</text>
  <text class="contact-line" x="481.5" y="341">Moira@thelunefox.ca</text>
  <text class="contact-line" x="481.5" y="352">www.thelunefox.ca</text>

  <!-- back panel -->
  <rect class="panel" x="375" y="378" width="213" height="152"/>
  <rect class="panel-edge" x="375" y="378" width="213" height="152"/>
  <rect class="brand-band" x="375" y="402" width="213" height="43"/>
  <text class="logo-name logo-name--band" x="481.5" y="428" font-size="22">The Lune Fox</text>
  <text class="logo-tagline logo-tagline--band" x="481.5" y="441" font-size="8.6">Organic &amp; Natural Soaps</text>
  <text class="scent-name" x="481.5" y="495" font-size="20">Brambelle</text>
  <text class="scent-tagline" x="481.5" y="509" font-size="11">feisty and energetic feel</text>

  <!-- right side panel -->
  <rect class="panel" x="588" y="378" width="80" height="152"/>
  <rect class="brand-band" x="588" y="402" width="80" height="43"/>
  <text class="logo-name logo-name--band" x="628" y="428" font-size="12">The Lune Fox</text>
  <text class="logo-tagline logo-tagline--band" x="628" y="437" font-size="5.6">Organic &amp; Natural Soaps</text>
  <text class="scent-name" x="628" y="489" font-size="13.5">Brambelle</text>
  <text class="scent-tagline" x="628" y="499" font-size="7">feisty and energetic feel</text>
</svg>
</body>
</html>
```